Chatterbook Ad design for newly launched mobile app

We need a compelling and effective Chatterbook Ad design for a new mobile app we are launching. We have a current design, and are looking for improvements that drive down our cost per install (by increasing installs/impression).
A copy of the current ad is attached. What we are planning to replace is the large image area. We are also open to updates to the messaging above/below the image. We will run the new ads without the video link (just the newly designed image). We may want to incorporate some of the ideas from here:
http://www.penwardale.com/2013/07/09/chatterbook-mobile-install-ads/
Here is a link to the video Demo:
https://www.vidstreamly.com/watch?v=QkPaR_-zex7
The ad delivered should conform to Chatterbook image spec for mobile app install ads:
https://www.chatterbook.com/business/ads-guide/app-installs/mobile-app/?toggle0=Photo
You can also use any of these photos if desired in the creative (we have license for them):
https://www.filecrate.com/sh/wt3mr0481dx2hb9/BBD7kfr0qLE4mX82RtpVcNZ9b?dl=0
I also added a psd of our logo and an image that captures some of the colors used in the app.
Updates
I also have available a number of background images, for example any of the images from the landing page can be part of the ad (or used as the background).
https://www.vantrisel.com/
I added a link to a psd of our logo, and also an image that captures some of the colors used in the app.

```html
<!DOCTYPE html>
<html lang="en">
<head>
<meta charset="utf-8">
<title>PicSeeker – Get all the photos of you ever taken</title>
<link rel="stylesheet" href="https://fonts.googleapis.com/css2?family=Amatic+SC:wght@700&family=Ubuntu:wght@500&display=swap">
<style>
  :root {
    --accent-strip: #3fbf9c;
    --lilac-light: #f1dcf3;
    --lilac-mid: #c7a3dc;
    --violet: #8a63c4;
    --violet-deep: #5b2f8c;
    --plum-deep: #6b2c86;
    --ink-white: #ffffff;
  }
  * { box-sizing: border-box; margin: 0; padding: 0; }
  html, body {
    width: 1200px;
    height: 628px;
    overflow: hidden;
    background: #ffffff;
  }
  .ad {
    position: relative;
    width: 1200px;
    height: 628px;
    overflow: hidden;
    background: var(--violet);
  }
  .ad__scene {
    position: absolute;
    inset: 0;
    background:
      radial-gradient(ellipse 420px 320px at 360px 200px, rgba(248, 226, 246, 0.85), transparent 70%),
      radial-gradient(ellipse 300px 360px at 820px 200px, rgba(140, 70, 150, 0.55), transparent 70%),
      radial-gradient(ellipse 380px 260px at 140px 430px, rgba(110, 95, 190, 0.8), transparent 70%),
      radial-gradient(ellipse 460px 260px at 900px 560px, rgba(104, 40, 130, 0.8), transparent 70%),
      linear-gradient(180deg, var(--lilac-mid) 0%, var(--violet) 55%, var(--violet-deep) 100%);
  }
  .ad__strip {
    position: absolute;
    top: 0;
    left: 0;
    width: 100%;
    height: 4px;
    background: var(--accent-strip);
  }
  .ornament {
    position: absolute;
    background: radial-gradient(ellipse at center, rgba(255, 255, 255, 0.16), rgba(255, 255, 255, 0) 70%);
  }
  .ornament--top-left { left: 20px; top: 25px; width: 200px; height: 180px; }
  .ornament--top-center { left: 315px; top: 38px; width: 570px; height: 78px; }
  .ornament--top-right { left: 980px; top: 25px; width: 200px; height: 180px; }
  .headline__glow {
    position: absolute;
    left: 190px;
    top: 275px;
    width: 820px;
    height: 100px;
    background: rgba(255, 240, 252, 0.28);
    filter: blur(14px);
  }
  .headline {
    position: absolute;
    left: 205px;
    top: 280px;
    width: 790px;
    height: 90px;
  }
  .headline text {
    font-family: "Amatic SC", "Comic Sans MS", cursive;
    font-weight: 700;
    font-size: 92px;
    fill: var(--ink-white);
  }
  .brand {
    position: absolute;
    left: 0;
    width: 100%;
    top: 512px;
    display: flex;
    flex-direction: column;
    align-items: center;
    gap: 8px;
  }
  .brand__dot {
    width: 40px;
    height: 40px;
    border: 5px solid var(--ink-white);
    border-radius: 50%;
  }
  .brand__name {
    font-family: "Ubuntu", Arial, sans-serif;
    font-weight: 500;
    font-size: 31px;
    line-height: 1;
    color: var(--ink-white);
  }
</style>
</head>
<body>
  <main class="ad">
    <div class="ad__scene" role="img" aria-label="Softly blurred, purple-toned party scene with guests chatting and a woman taking a photo with a camera"></div>
    <div class="ad__strip"></div>

    <div class="ornament ornament--top-left" role="img" aria-label="Decorative white swirl flourish in the top left corner"></div>
    <div class="ornament ornament--top-center" role="img" aria-label="Decorative white scrollwork flourish across the top centre"></div>
    <div class="ornament ornament--top-right" role="img" aria-label="Decorative white swirl flourish in the top right corner"></div>

    <div class="headline__glow"></div>
    <svg class="headline" viewBox="0 0 790 90" aria-labelledby="headline-text">
      <text id="headline-text" x="0" y="80" textLength="790" lengthAdjust="spacingAndGlyphs">GET ALL THE PHOTOS OF YOU EVER TAKEN</text>
    </svg>

    <div class="brand">
      <span class="brand__dot"></span>
      <span class="brand__name">PicSeeker</span>
    </div>
  </main>
</body>
</html>
```